Unique business card design

We are looking for a design that reflects our unique social media and online marketing agency "Kestrel Media". We are a young agency with a focus on speakers, coaches and trainers. In other words, we support people who want to do good with their work and help other people live a happier, more successful and fulfilling life, reach as many people as possible with their work and thus have an influence. Our values are: sustainability, creating added value, individuality, proactivity. We want our clients to feel comfortable with us and that's why the relationship with them is very important to us. We want every customer to become a lifelong friend of the company. Most of our clients are premium coaches, meaning they are in the higher priced segment and expect seriousness, professionalism and quality. All of these things should reflect our business card as well. I look forward to feedback. Best regards, Tomas Wylander

```html
<!DOCTYPE html>
<html lang="en">
<head>
<meta charset="utf-8">
<title>Kestrel Media – Business Card</title>
<link rel="stylesheet" href="https://fonts.googleapis.com/css2?family=Montserrat:wght@700&family=Questrial&display=swap">
<style>
  :root {
    --canvas: #d6d6d6;
    --card: #f7f7f8;
    --navy: #1a1a4e;
    --ink: #14143c;
    --deep: #0f0f2e;
    --royal: #2c2f80;
    --blue: #1e73be;
    --tagline: #3b3aa0;
    --text: #1c1c1c;
  }
  * { margin: 0; padding: 0; box-sizing: border-box; }
  html, body { width: 900px; height: 1200px; overflow: hidden; }
  body {
    position: relative;
    background: var(--canvas);
    font-family: "Questrial", "Century Gothic", sans-serif;
    color: var(--text);
  }
  .card {
    position: absolute;
    left: 80px;
    width: 740px;
    height: 434px;
    border-radius: 30px;
    background: var(--card);
    overflow: hidden;
  }
  .card--front { top: 133px; }
  .card--back { top: 636px; }

  .facet-band {
    position: absolute;
    left: 0;
    width: 100%;
    background: linear-gradient(100deg, var(--deep) 0%, var(--navy) 30%, var(--royal) 55%, var(--blue) 80%, #2a6fc0 100%);
  }
  .card--front .facet-band--top { top: 0; height: 115px; }
  .card--front .facet-band--foot { bottom: 0; height: 24px; }
  .card--back .facet-band--top { top: 0; height: 310px; }

  .holder { position: absolute; left: 35px; top: 30px; }
  .holder__name {
    font-family: "Montserrat", "Arial", sans-serif;
    font-weight: 700;
    font-size: 34px;
    letter-spacing: 1px;
    color: #fff;
    line-height: 1;
  }
  .holder__role {
    margin-top: 12px;
    font-size: 22px;
    color: var(--blue);
    line-height: 1;
  }

  .brand { position: absolute; display: flex; flex-direction: column; align-items: flex-start; }
  .brand__mark { width: 150px; height: 112px; background: var(--navy); border: 6px solid #fff; }
  .brand__name {
    margin-top: 6px;
    font-size: 40px;
    color: var(--navy);
    line-height: 1.05;
    white-space: nowrap;
  }
  .brand__tagline {
    margin-top: 4px;
    font-size: 16px;
    color: var(--tagline);
    letter-spacing: 0.3px;
    white-space: nowrap;
  }
  .card--front .brand { left: 428px; top: 40px; }
  .card--back .brand { left: 228px; top: 228px; }

  .divider {
    position: absolute;
    left: 37px; top: 269px;
    width: 660px; height: 2px;
    background: var(--navy);
  }

  .contact { position: absolute; left: 37px; top: 288px; list-style: none; }
  .contact__item {
    display: flex; align-items: center; gap: 13px;
    height: 29px;
    font-size: 17px;
  }
  .contact__icon { width: 20px; height: 20px; flex: none; }

  .address {
    position: absolute; right: 43px; top: 288px;
    font-style: normal; text-align: right;
    font-size: 17px; line-height: 29px;
  }
</style>
</head>
<body>

  <section class="card card--front" aria-label="Business card front">
    <div class="facet-band facet-band--top" role="img" aria-label="Abstract faceted pattern in navy and blue"></div>
    <div class="facet-band facet-band--foot" role="img" aria-label="Abstract faceted pattern strip"></div>

    <header class="holder">
      <h1 class="holder__name">JONAS HARTLEY</h1>
      <p class="holder__role">PRESIDENT</p>
    </header>

    <div class="brand">
      <div class="brand__mark"></div>
      <p class="brand__name">Kestrel Media</p>
      <p class="brand__tagline">Online Marketing Services</p>
    </div>

    <div class="divider"></div>

    <ul class="contact">
      <li class="contact__item">
        <svg class="contact__icon" viewBox="0 0 20 20" aria-hidden="true">
          <rect width="20" height="20" rx="3" fill="#1a1a4e"/>
          <path d="M4 8c0-2 2.5-3 6-3s6 1 6 3l-2 1-1-2H7L6 9z" fill="#fff"/>
          <rect x="6" y="10" width="8" height="5" rx="1" fill="#fff"/>
        </svg>
        <span>403-555-0148</span>
      </li>
      <li class="contact__item">
        <svg class="contact__icon" viewBox="0 0 20 20" aria-hidden="true">
          <rect width="20" height="20" rx="3" fill="#1a1a4e"/>
          <rect x="4" y="6" width="12" height="8" fill="#fff"/>
          <path d="M4 6l6 5 6-5M4 14l4.5-4M16 14l-4.5-4" fill="none" stroke="#1a1a4e" stroke-width="1"/>
        </svg>
        <span>Jonashartley@kestrelmedia.com</span>
      </li>
      <li class="contact__item">
        <svg class="contact__icon" viewBox="0 0 20 20" aria-hidden="true">
          <rect width="20" height="20" rx="3" fill="#1a1a4e"/>
          <circle cx="10" cy="10" r="6" fill="none" stroke="#fff" stroke-width="1.2"/>
          <ellipse cx="10" cy="10" rx="2.6" ry="6" fill="none" stroke="#fff" stroke-width="1"/>
          <path d="M4 10h12M5 7h10M5 13h10" stroke="#fff" stroke-width="0.9"/>
        </svg>
        <span>www.kestrelmedia.com</span>
      </li>
    </ul>

    <address class="address">
      310, 845- 9th Ave, SW<br>
      Calgary,ab, T2P 1L4
    </address>
  </section>

  <section class="card card--back" aria-label="Business card back">
    <div class="facet-band facet-band--top" role="img" aria-label="Abstract faceted pattern in navy and blue"></div>
    <div class="brand">
      <div class="brand__mark"></div>
      <p class="brand__name">Kestrel Media</p>
      <p class="brand__tagline">Online Marketing Services</p>
    </div>
  </section>

</body>
</html>
```